Business Card Design for Lawn Management

Lawn Management

Industry/Entity Type

Business

Contact Information for Business Card

Calloway Lawn Management
Doran Calloway
Calloway_Lawn@brindlemail.com
404-627-1845

```html
<!DOCTYPE html>
<html lang="en">
<head>
<meta charset="utf-8">
<title>Calloway Lawn Management – Business Card</title>
<link rel="stylesheet" href="https://fonts.googleapis.com/css2?family=Arimo&family=Oswald:wght@600&family=Tinos&display=swap">
<style>
  :root {
    --page: #ffffff;
    --frame: #1a1a1a;
    --brand-green: #3a952f;
    --leaf-green: #47a53a;
    --swoosh-light: #a6d13c;
    --swoosh-dark: #6cb52d;
    --mark-grey: #d1d2d4;
    --back-top: #a7a9ac;
    --back-bottom: #ffffff;
    --back-text: #ffffff;
    --name-text: #faf8e4;
    --name-glow: #e9e7a6;
  }
  html, body {
    margin: 0;
    padding: 0;
    width: 1020px;
    height: 1200px;
    overflow: hidden;
    background: var(--page);
  }
  .card-sheet {
    display: block;
    width: 1020px;
    height: 1200px;
  }
  .trim-frame { fill: none; stroke: var(--frame); stroke-width: 2; }
  .card-face { fill: var(--page); stroke: var(--frame); stroke-width: 1.5; }
  .wordmark {
    font-family: "Oswald", "Arial Narrow", sans-serif;
    font-weight: 600;
    font-size: 120px;
    fill: var(--brand-green);
  }
  .tagline {
    font-family: "Arimo", Arial, sans-serif;
    font-size: 27px;
    fill: var(--brand-green);
  }
  .mark-dot { fill: var(--leaf-green); }
  .mark-dot--faint { fill: var(--mark-grey); }
  .back-face { fill: url(#backGradient); stroke: var(--frame); stroke-width: 1.5; }
  .person-name {
    font-family: "Tinos", "Times New Roman", serif;
    font-size: 44px;
    fill: var(--name-text);
    filter: url(#nameGlow);
  }
  .company-name {
    font-family: "Tinos", "Times New Roman", serif;
    font-size: 46px;
    fill: var(--back-text);
  }
  .divider { stroke: var(--back-text); stroke-width: 4; }
  .contact-band { fill: var(--brand-green); }
  .contact-email {
    font-family: "Arimo", Arial, sans-serif;
    font-size: 26px;
    fill: var(--back-text);
  }
  .contact-phone {
    font-family: "Tinos", "Times New Roman", serif;
    font-size: 28px;
    fill: var(--back-text);
  }
</style>
</head>
<body>
<svg class="card-sheet" viewBox="0 0 1054 1240" preserveAspectRatio="none" xmlns="http://www.w3.org/2000/svg">
  <defs>
    <linearGradient id="swooshGradient" x1="0" y1="0" x2="0" y2="1">
      <stop offset="0" stop-color="var(--swoosh-dark)"/>
      <stop offset="0.4" stop-color="var(--swoosh-light)"/>
      <stop offset="1" stop-color="var(--swoosh-dark)"/>
    </linearGradient>
    <linearGradient id="backGradient" x1="0" y1="0" x2="0" y2="1">
      <stop offset="0" stop-color="var(--back-top)"/>
      <stop offset="1" stop-color="var(--back-bottom)"/>
    </linearGradient>
    <filter id="nameGlow" x="-20%" y="-40%" width="140%" height="180%">
      <feGaussianBlur in="SourceAlpha" stdDeviation="3" result="blur"/>
      <feFlood flood-color="var(--name-glow)"/>
      <feComposite in2="blur" operator="in" result="glow"/>
      <feMerge><feMergeNode in="glow"/><feMergeNode in="glow"/><feMergeNode in="SourceGraphic"/></feMerge>
    </filter>
  </defs>

  <!-- Front of card -->
  <g class="card-front">
    <rect class="trim-frame" x="2" y="2" width="1050" height="600"/>
    <rect class="card-face" x="20" y="20" width="1014" height="564"/>
    <path class="swoosh" fill="url(#swooshGradient)"
          d="M402,22 C300,32 228,92 222,205 C216,325 318,450 384,550 C305,440 244,322 240,212 C237,105 300,45 402,22 Z"/>
    <circle class="mark-dot mark-dot--faint" cx="895" cy="125" r="92"/>
    <circle class="mark-dot" cx="180" cy="440" r="90"/>
    <text class="wordmark" x="472" y="328" textLength="416" lengthAdjust="spacingAndGlyphs">CALLOWAY</text>
    <text class="tagline" x="888" y="361" text-anchor="end">Lawn Management</text>
  </g>

  <!-- Back of card -->
  <g class="card-back">
    <rect class="trim-frame" x="2" y="638" width="1050" height="600"/>
    <rect class="back-face" x="20" y="656" width="1014" height="564"/>
    <text class="person-name" x="985" y="735" text-anchor="end">Doran Calloway</text>
    <text class="person-name" x="985" y="790" text-anchor="end">Calloway</text>
    <text class="company-name" x="272" y="922" text-anchor="middle">Calloway Lawn</text>
    <text class="company-name" x="267" y="977" text-anchor="middle">Management,</text>
    <line class="divider" x1="480" y1="853" x2="480" y2="1022"/>
    <circle class="mark-dot" cx="925" cy="1112" r="70"/>
    <polygon class="contact-band" points="20,1122 452,1122 494,1192 1034,1192 1034,1220 20,1220"/>
    <text class="contact-email" x="36" y="1162" textLength="400" lengthAdjust="spacingAndGlyphs">Calloway_Lawn@brindlemail.com</text>
    <text class="contact-phone" x="412" y="1198" text-anchor="end">404-627-1845</text>
  </g>
</svg>
</body>
</html>
```